"Tolvar" (spanish restaurant) "Bar de Tapas"

"Tolvar" is a spanish restaurant located in the city of Santo Domingo, Dominican Republic. It needs a new and fresh idea for its business card. I would like to take the idea of one of the spaces of the restaurant represented on a business card, for example, the blue and emblematic entrance door of the restaurant, or maybe the bricks on the main room of the restaurant, or how about the bar. Any idea it's good! I invite all the creative designers to participate on the suggestions of it.

What doe sit need? It needs this information on it:

Name: Tolvar
Business: Restaurante
Address: Ruth P Caldera 00, Bellavento
Phone number: 809-555-0147
website: www.tolvarrestaurante.example

Reason: NEED MORE OPTION FOR IT. I WANT YOU TO EXPRESS YOUR DESIGN AS YOU WANT TO NOT AS I ASK YOU TO.

Industry/Entity Type

Restaurant

Contact Information for Business Card

c/Ruth P Caldera 47

Requirements
Must have
• Creativity. I'm open to new and fresh ideas.
Nice to have
• The entrance door (blue one) would be a plus in the design of the card. Maybe the background could be images of materials like bricks or wood, like the ones in the pictures of the restaurant.

```html
<!DOCTYPE html>
<html lang="es">
<head>
<meta charset="utf-8">
<title>Tolvar — Business Card</title>
<link rel="stylesheet" href="https://fonts.googleapis.com/css2?family=Open+Sans:wght@400;600;700&display=swap">
<style>
  :root {
    --backdrop: #8e8e8e;
    --orange: #ee4323;
    --black: #050505;
    --white: #ffffff;
    --card-w: 600px;
    --card-h: 343px;
  }
  * { box-sizing: border-box; margin: 0; padding: 0; }
  html, body { width: 1200px; height: 900px; overflow: hidden; }
  body {
    position: relative;
    background: var(--backdrop);
    font-family: "Open Sans", Arial, sans-serif;
    color: var(--white);
  }
  .card {
    position: absolute;
    width: var(--card-w);
    height: var(--card-h);
    overflow: hidden;
    box-shadow: 0 6px 18px rgba(0,0,0,.25);
  }
  .card--front { left: 330px; top: 80px; background: var(--orange); }
  .card--back  { left: 210px; top: 470px; background: var(--orange); }

  /* front */
  .front__band {
    position: absolute; left: 0; right: 0;
    top: 20%; height: 63%;
    background: var(--black);
    display: flex; align-items: center; justify-content: center;
  }
  .brand-name {
    font-weight: 700;
    letter-spacing: 2px;
    text-transform: uppercase;
    line-height: 1;
  }
  .front__band .brand-name { font-size: 72px; color: var(--white); }

  /* back */
  .back__top {
    position: absolute; left: 0; right: 0; top: 0; height: 40%;
    background: var(--black);
  }
  .back__top .brand-name {
    position: absolute; right: 70px; top: 50px;
    font-size: 64px; color: var(--orange);
  }
  .back__bottom {
    position: absolute; left: 0; right: 0; bottom: 0; height: 7%;
    background: var(--black);
  }
  .person {
    position: absolute; left: 22px; top: 25%;
  }
  .person__name { font-size: 22px; font-weight: 700; line-height: 1.2; }
  .person__role { font-size: 13px; font-weight: 400; }
  .contact {
    position: absolute; right: 22px; top: 50%;
    list-style: none;
    text-align: right;
    font-size: 17px;
    line-height: 24px;
  }
  .contact li { display: flex; justify-content: flex-end; align-items: center; gap: 10px; }
  .contact svg { width: 14px; height: 14px; fill: var(--white); flex: none; }
</style>
</head>
<body>

<section class="card card--front" aria-label="Tolvar business card, front">
  <div class="front__band">
    <span class="brand-name">Tolvar</span>
  </div>
</section>

<section class="card card--back" aria-label="Tolvar business card, back">
  <div class="back__top">
    <span class="brand-name">Tolvar</span>
  </div>
  <div class="person">
    <p class="person__name">Elena Varga</p>
    <p class="person__role">Managing Director</p>
  </div>
  <ul class="contact">
    <li>809-555-0147
      <svg viewBox="0 0 16 16" aria-hidden="true"><path d="M2 6c0-2 3-3 6-3s6 1 6 3v1h-3V5.5c-1-.4-5-.4-6 0V7H2z"/><rect x="4" y="8" width="8" height="5" rx="1"/></svg></li>
    <li>809-555-0147
      <svg viewBox="0 0 16 16" aria-hidden="true"><rect x="4" y="1" width="8" height="14" rx="1.5"/></svg></li>
    <li>info@tolvarrestaurante.example
      <svg viewBox="0 0 16 16" aria-hidden="true"><path d="M1 3h14v10H1z M1 3l7 6 7-6" /></svg></li>
    <li>www.tolvarrestaurante.example
      <svg viewBox="0 0 16 16" aria-hidden="true"><path d="M6 10l4-4 1 1-4 4z M3 9l3-3 2 1-3 3 2 2 3-3 1 2-3 3a2 2 0 0 1-3 0l-2-2a2 2 0 0 1 0-3z"/></svg></li>
    <li>c/Ruth P Caldera 47, Bellavento
      <svg viewBox="0 0 16 16" aria-hidden="true"><path d="M8 1a5 5 0 0 1 5 5c0 4-5 9-5 9S3 10 3 6a5 5 0 0 1 5-5zm0 3a2 2 0 1 0 0 4 2 2 0 0 0 0-4z"/></svg></li>
  </ul>
  <div class="back__bottom"></div>
</section>

</body>
</html>
```